One of Australia's fastest growing Financial Company looking for an updated business card design!

Meridale Holdings Australia is looking for an updated design for our business cards. We would like to keep up our professional appearances and have get new exciting design that fits our company.

The Meridale aim is to facilitate and assist clients in every financial requirement that may arise in financial areas.

We would to see the design to use colour blue and we like the clouds in the background. We have attached two designs we have use before but we need something with more professional and easy to read design.

We would like the website in the back of the card; the employees name more central and stands out; only a postal address; a list of all our locations along the bottom (Sydney, Melbourne, Brisbane, Singapore)

Looking forward to seeing the designs come in!

Target Market(s)

Other Industry Professionals
Middle Class Families

Industry/Entity Type

Finance

Contact Information for Business Card

Name; Company Role; Office Number; Mobile Number; Email Address; Website; Postal Address; Locations

Font styles to use
Serif
Sans Serif

Colors
0492cd
33a6d7
85cae6
85acd3
3176b5
0455a3
cee9f5
d5e2ee

Requirements
Must have
• Name; Company Role; Office Number; Mobile Number; Email Address; Website; Postal Address; Locations
Nice to have
• The colour blue, clouds on the background

```html
<!DOCTYPE html>
<html lang="en">
<head>
<meta charset="utf-8">
<title>Meridale Holdings Australia – Business Card</title>
<link href="https://fonts.googleapis.com/css2?family=Ubuntu:wght@400;500&display=swap" rel="stylesheet">
<style>
  :root {
    --stage: #2a2a2c;
    --card-white: #f7f7f7;
    --brand-blue: #0492cd;
    --sky-top: #85cae6;
    --sky-mid: #33a6d7;
    --sky-light: #cee9f5;
    --accent-red: #d9322e;
    --ink: #3a3a3c;
    --icon-blue: #85cae6;
  }
  * { box-sizing: border-box; margin: 0; padding: 0; }
  html, body { width: 1200px; height: 900px; overflow: hidden; }
  body {
    background: var(--stage);
    font-family: "Ubuntu", sans-serif;
    position: relative;
  }
  .card {
    position: absolute;
    left: 250px;
    width: 700px;
    height: 400px;
    border-radius: 4px;
    box-shadow: 0 12px 30px rgba(0,0,0,.5);
    overflow: hidden;
  }
  .card-back { top: 40px; }
  .card-front { top: 460px; background: var(--card-white); }

  .sky {
    position: absolute; inset: 0;
    background:
      radial-gradient(ellipse 220px 110px at 68% 22%, rgba(255,255,255,.85), rgba(255,255,255,0) 70%),
      radial-gradient(ellipse 160px 80px at 40% 30%, rgba(255,255,255,.45), rgba(255,255,255,0) 70%),
      linear-gradient(160deg, var(--sky-light) 0%, var(--sky-top) 45%, var(--sky-mid) 100%);
  }
  .back-brand {
    position: absolute; left: 0; right: 0; top: 150px;
    display: flex; align-items: center; justify-content: center; gap: 18px;
  }
  .back-brand .mark {
    width: 48px; height: 48px; border-radius: 50%;
    background: var(--accent-red);
  }
  .back-brand .name {
    font-size: 84px; font-weight: 500; color: #ffffff; letter-spacing: 1px;
  }
  .back-web {
    position: absolute; left: 0; right: 0; top: 262px;
    text-align: center; font-size: 20px; color: var(--accent-red);
  }

  .front-brand {
    position: absolute; left: 48px; top: 52px;
    display: flex; align-items: center; gap: 12px;
  }
  .front-brand .mark {
    width: 30px; height: 30px; border-radius: 50%; background: var(--accent-red);
  }
  .front-brand .name {
    font-size: 44px; font-weight: 500; color: var(--brand-blue);
  }
  .person {
    position: absolute; right: 44px; top: 58px; text-align: right;
  }
  .person .full-name {
    font-size: 30px; color: var(--ink); letter-spacing: .5px;
  }
  .person .role {
    font-size: 16px; color: var(--accent-red); margin-top: 2px;
  }
  .contacts {
    position: absolute; left: 48px; top: 180px;
    list-style: none;
  }
  .contacts li {
    display: flex; align-items: center; gap: 16px;
    font-size: 19px; color: var(--ink); height: 30px;
  }
  .contacts svg { width: 18px; height: 18px; flex: none; }
  .contacts .indent { padding-left: 34px; }
</style>
</head>
<body>
  <section class="card card-back">
    <div class="sky" role="img" aria-label="Soft blue sky with white clouds"></div>
    <div class="back-brand">
      <span class="mark"></span>
      <span class="name">Meridale</span>
    </div>
    <div class="back-web">www.meridaleholdingsgroup.com.au</div>
  </section>

  <section class="card card-front">
    <div class="front-brand">
      <span class="mark"></span>
      <span class="name">Meridale</span>
    </div>
    <div class="person">
      <div class="full-name">CLARA HENSLEY</div>
      <div class="role">Investment Consultant</div>
    </div>
    <ul class="contacts">
      <li>
        <svg viewBox="0 0 24 24" fill="var(--icon-blue)"><path d="M6.6 10.8a15 15 0 006.6 6.6l2.2-2.2a1 1 0 011-.25 11.4 11.4 0 003.6.6 1 1 0 011 1V20a1 1 0 01-1 1A17 17 0 013 4a1 1 0 011-1h3.5a1 1 0 011 1 11.4 11.4 0 00.6 3.6 1 1 0 01-.25 1z"/></svg>
        (02) 5550 1847
      </li>
      <li>
        <svg viewBox="0 0 24 24" fill="none" stroke="var(--icon-blue)" stroke-width="2"><rect x="7" y="2" width="10" height="20" rx="2"/><line x1="11" y1="18" x2="13" y2="18"/></svg>
        (04) 555 018 266
      </li>
      <li>
        <svg viewBox="0 0 24 24" fill="var(--icon-blue)"><path d="M2 6h20v12H2z"/><path d="M2 6l10 7 10-7" stroke="#fff" stroke-width="1.6" fill="none"/></svg>
        info@meridaleholdingsgroup.com.au
      </li>
      <li>
        <svg viewBox="0 0 24 24" fill="none" stroke="var(--icon-blue)" stroke-width="2"><circle cx="12" cy="12" r="9"/><path d="M3 12h18M12 3a14 14 0 010 18M12 3a14 14 0 000 18"/></svg>
        www.meridaleholdingsgroup.com.au
      </li>
      <li>
        <svg viewBox="0 0 24 24" fill="var(--icon-blue)"><path d="M12 2a7 7 0 00-7 7c0 5 7 13 7 13s7-8 7-13a7 7 0 00-7-7zm0 9.5A2.5 2.5 0 1112 6.5a2.5 2.5 0 010 5z"/></svg>
        Harbourview Post Shop PO BOX 4180
      </li>
      <li class="indent">(Sydney, Melbourne, Brisbane, Singapore)</li>
    </ul>
  </section>
</body>
</html>
```